Riverbend Haven Home Care-Nursing Assessment Form

I am creating a Nursing Assessment Form (which is used to be an intake form for all new patients) for my new home care company, Riverbend Haven Home Care.

It is 15 pages and pretty comprehensive as this is a very regulated field. I have all the necessary content and information attached in the word document below. Now, I am seeking a designer to make it look professional, cohesive and easy to read/ follow.
In order for your Word Document Design to be selected, you must:

1. As mentioned previously, make it easy to read/follow. There should be enough spacing, room to write out all necessary notes, fill out check marks...etc...
2. It should look professional.
3. It should be attractive and eye pleasing. Attached you will find our logo-kindly incorporate it's style into the project as well. The logo should be placed on top of each page.
4. Lastly, we need a Word Document version AND PDF Fillable Option. The fillable PDF should Auto Fill for the Name and Start of Care (SOC) Date.

I have attached a sample form below as well. This is how I envision the finished project to look. Of course, I am open to other suggestions as look as it meets the aforementioned requirements.

Thank you! May the best man or woman win!
Our team looks forward to working with our designer on this project!

Industry/Entity Type

Home Health Care

Font styles to use
Sans Serif

Colors
0255a3
9bcb3c

Requirements
Must have
• Refer to Project Description above.
Nice to have
We must be given a Word Document Option and PDF Fillable Option.

```html
<!DOCTYPE html>
<html lang="en">
<head>
<meta charset="utf-8">
<title>Riverbend Haven Home Care – Initial Assessment Form</title>
<link href="https://fonts.googleapis.com/css2?family=Questrial&display=swap" rel="stylesheet">
<style>
  :root{
    --brand-blue:#0255a3;
    --brand-green:#9bcb3c;
    --bar-blue:#4f86cf;
    --paper:#f5f5f5;
    --ink:#333333;
    --rule:#6a6a6a;
    --stage:#e9ecf1;
  }
  *{margin:0;padding:0;box-sizing:border-box}
  html,body{width:1200px;height:900px;overflow:hidden}
  body{background:var(--stage);font-family:"Questrial",Arial,sans-serif;color:var(--ink);position:relative}
  .page{position:absolute;top:60px;width:578px;height:781px;background:var(--paper);box-shadow:0 4px 14px rgba(0,0,0,.12)}
  .page--one{left:14px}
  .page--two{left:608px}
  .block{position:absolute;left:69px;right:52px;font-size:7.6px;line-height:12.6px}
  .brand{position:absolute;top:22px;left:0;right:0;display:flex;justify-content:center;align-items:center;gap:5px;color:var(--brand-blue);font-size:9px}
  .brand-dot{width:12px;height:12px;border-radius:50%;background:var(--brand-green)}
  .title{position:absolute;top:70px;left:0;right:0;text-align:center;font-size:9.6px;line-height:12px;color:#222}
  .name-row{position:absolute;top:106px;left:69px;right:52px;font-size:11px;display:flex}
  .name-row .soc{position:absolute;left:335px}
  .u{display:inline-block;border-bottom:.7px solid var(--rule);height:9px;vertical-align:bottom}
  .rule{border-bottom:.7px solid var(--rule);height:8px;margin-bottom:2px}
  .b{font-weight:700}
  .bar{position:absolute;left:69px;width:190px;height:17px;line-height:17px;padding-left:7px;background:var(--bar-blue);color:#fff;font-size:8.4px;font-weight:700;letter-spacing:.1px}
  .bar--short{width:76px}
  .footer{position:absolute;top:739px;height:3px}
  .footer--blue{left:69px;width:143px;background:var(--brand-blue)}
  .footer--green{left:216px;width:330px;background:var(--brand-green)}
  .risk-box{position:absolute;left:439px;top:418px;width:126px;height:170px;border:.8px solid #777;padding:4px 5px;font-size:7.4px;line-height:13px}
  .risk-box i{font-style:italic}
  .quiz{position:absolute;left:87px;top:458px;width:345px;font-size:7.5px;line-height:13px;list-style:none}
  .quiz li{display:flex}
  .quiz .n{width:17px;text-align:right;padding-right:6px}
  .quiz .t{width:300px}
  .quiz .v{margin-left:12px}
  .cols{display:flex;justify-content:space-between}
</style>
</head>
<body>

<section class="page page--one">
  <div class="brand"><span class="brand-dot"></span>Riverbend Haven Home Care</div>
  <div class="title">Riverbend Haven Home Care<br>Initial Assessment Form</div>
  <div class="name-row">Name&nbsp;<span class="u" style="width:154px;height:11px"></span><span class="soc">SOC Date</span></div>

  <div class="block b" style="top:137px;left:75px;font-size:7.4px;line-height:10px">
    Patient's Name<span class="u" style="width:210px"></span>Gender<span class="u" style="width:24px"></span>MR#<span class="u" style="width:60px"></span>Date<span class="u" style="width:12px"></span><br>
    Primary Diagnosis<span class="u" style="width:200px"></span>Secondary Diagnosis <span class="u" style="width:54px"></span> Other<br>
    Pertinent Diagnosis<span class="u" style="width:251px"></span>PCP name <span class="u" style="width:41px"></span>Other<br>
    Physician Name <span class="u" style="width:260px"></span>
  </div>
  <div class="block" style="top:182px;font-size:7.4px;line-height:10.5px">
    <span class="b">Prognosis:</span> ( &nbsp;) Poor &nbsp;&nbsp;&nbsp;&nbsp;&nbsp;&nbsp;&nbsp; ( &nbsp;) Fair &nbsp;&nbsp;&nbsp;&nbsp;&nbsp;&nbsp; ( &nbsp;) Good ( ) Excellent<br>
    &nbsp;<span class="b">Vital Signs</span> &nbsp;Height:<span class="u" style="width:42px"></span> &nbsp;&nbsp;&nbsp;Weight:<span class="u" style="width:34px"></span> &nbsp;&nbsp;&nbsp;Temp:<span class="u" style="width:34px"></span> &nbsp;&nbsp;&nbsp;Pulse:<span class="u" style="width:34px"></span> &nbsp;&nbsp;&nbsp;Resp:<span class="u" style="width:34px"></span> &nbsp;&nbsp;&nbsp;B/P:<span class="u" style="width:38px"></span>
  </div>
  <div class="block b" style="top:212px;font-size:7.4px;line-height:13px">
    Allergies:<span class="u" style="width:220px"></span><br>
    &nbsp;Past Medical &amp; Surgical History:<span class="u" style="width:340px"></span>
    <div class="rule" style="height:6px"></div>
  </div>

  <div class="bar" style="top:250px">Support System</div>
  <div class="block" style="top:268px">
    Married/Not Married/Single/Divorced/Widowed<br>
    Lives Alone: ( &nbsp;) Yes &nbsp;( &nbsp;) No<br>
    Family Composition:<span class="u" style="width:262px"></span><br>
    Legal Next of Kin:<span class="u" style="width:163px"></span>Telephone:<br>
    <span class="u" style="width:268px"></span>/<span class="u" style="width:110px"></span><br>
    Address:<span class="u" style="width:177px"></span>E-mail: <span class="u" style="width:108px"></span><br>
    &nbsp;Is significant other able, available, capable and<br>
    &nbsp;willing to care for patient? <span style="margin-left:128px">Yes &nbsp;&nbsp;No</span><br>
    If No, explain:
    <div class="rule" style="width:435px"></div>
    Educational Needs of Patient/Family:
    <div class="rule" style="width:462px;height:9px"></div>
  </div>

  <div class="bar" style="top:414px">Environment</div>
  <div class="block" style="top:434px">
    ( &nbsp;) Private Home<br>( &nbsp;) Apartment<br>( &nbsp;) Elevator<br>( &nbsp;) Walkup
  </div>

  <div class="bar" style="top:488px">Safety Hazards in the Home</div>
  <div class="block" style="top:508px;right:46px;line-height:9.6px">
    ( &nbsp;) Sound structure &nbsp;&nbsp;( &nbsp;) Safe Placement of Cords, Rugs and Furniture &nbsp;&nbsp;( &nbsp;) Adequate Heating and Ventilation &nbsp;&nbsp;( &nbsp;) Adequate Cooking facility<br>
    <span style="display:block;margin-top:3px">( &nbsp;) Adequate Plumbing/Sanitation/ Running Water ( &nbsp;) Adequate Sleeping Arrangement ( &nbsp;) Safe Gas/Electric Appliances ( &nbsp;)</span>
    <span style="display:block;margin-top:3px">Grounded Plug for Equipment ( ) Enough Electrical Outlets for Equipment ( ) Working Telephone in the Home</span>
    <span style="display:block;margin-top:3px">( ) Safe storage for Supplies/Equipment/Meds? ( ) &nbsp;Exits Free of Obstruction ( &nbsp;) Working smoke detectors? &nbsp;&nbsp;( &nbsp;) Fire extinguisher in home?</span>
    <span style="display:block;margin-top:3px">( &nbsp;) Infestations of pests? &nbsp;( &nbsp;) Neighborhood safe?</span>
    Comments:<span class="u" style="width:416px;height:7px"></span>
  </div>

  <div class="bar" style="top:603px">Caregiver's Contact Information</div>
  <div class="block" style="top:622px;line-height:12.2px">
    Name:<span class="u" style="width:199px"></span><br>
    Telephone<span class="u" style="width:143px"></span>/<span class="u" style="width:111px"></span><br>
    Address:<span class="u" style="width:177px"></span>E-mail:<span class="u" style="width:108px"></span><br>
    <span style="line-height:9px;display:block">Days / Time Available:<span class="u" style="width:380px"></span></span>
  </div>

  <div class="bar" style="top:673px">Caregiver's Ability to Assist Patient</div>
  <div class="block" style="top:692px">
    Personal Care: ( ) Yes ( ) No<br>Mobility: ( ) Yes ( ) No<br>Prepare/Serve Meals: ( ) Yes ( ) No
  </div>

  <div class="footer footer--blue"></div>
  <div class="footer footer--green"></div>
</section>

<section class="page page--two">
  <div class="brand"><span class="brand-dot"></span>Riverbend Haven Home Care</div>
  <div class="title">Riverbend Haven Home Care<br>Initial Assessment Form</div>
  <div class="name-row">Name&nbsp;<span class="u" style="width:157px;height:11px"></span><span class="soc" style="left:344px">SOC Date</span></div>

  <div class="block" style="top:132px;line-height:10px">
    Maintain Safe/Clean Environment: ( ) Yes ( ) No<br>
    <span style="display:block;margin-top:3px">Perform/ Assist with Procedures: &nbsp;( ) Yes ( ) No</span>
    Caregiver has capacity to learn therapeutic regimen: ( &nbsp;) Yes ( &nbsp;) No<br>
    Comments: <span class="u" style="width:430px;height:8px"></span>
  </div>

  <div class="block b" style="top:195px;line-height:10px">
    Are There Any Signs of Abuse or Neglect from Family or Caregiver? ( ) Yes ( &nbsp;) No<br>
    If Yes, describe:
    <div class="rule" style="width:483px;height:7px"></div>
    <div class="rule" style="width:483px;height:6px"></div>
    <div class="rule" style="width:483px;height:7px"></div>
    <div class="rule" style="width:57px;height:7px"></div>
  </div>

  <div class="bar" style="top:266px">Advanced Directive</div>
  <div class="block" style="top:285px;line-height:10.8px">
    Patient has a Living Will ( ) Yes ( ) No Health Care Proxy ( ) Yes ( ) No<br>
    Special Provisions Included: ( ) DNR ( ) DNI ( ) No Mech. Ventilation ( )<br>
    Med. Support Only ( ) No Feeding Tubes ( ) &nbsp;Copies of Documentation Attached ( ) Yes ( ) No<br>
    Other<span class="u" style="width:414px;height:8px"></span>
  </div>

  <div class="bar" style="top:337px">Nutritional</div>
  <div class="block" style="top:356px;line-height:13px">
    Diet: <span class="u" style="width:117px"></span><br>
    Meals Prepared By: <span class="u" style="width:107px"></span><br>
    Meals Patterns/Tolerance/Restrictions: <span class="u" style="width:128px"></span><br>
    Compliance: ( &nbsp;) Yes ( &nbsp;) No
  </div>
  <div class="block" style="top:420px;font-style:italic;line-height:13px">
    Statement:<br><span style="margin-left:55px">Value:</span>
  </div>

  <ol class="quiz">
    <li><span class="n">1.</span><span class="t">I have an illness or condition that made me change the kind and/or amount of food I eat- &nbsp;2</span><span class="v"></span></li>
    <li><span class="n">2.</span><span class="t">I eat fewer than two meals per day<br><span style="margin-left:22px">3</span></span><span class="v"></span></li>
    <li><span class="n">3.</span><span class="t">I do not eat fruits, vegetables or milk products</span><span class="v">2</span></li>
    <li><span class="n">4.</span><span class="t">I have three of more drinks of beer, liquor or wine almost every day<br><span style="margin-left:22px">2</span></span><span class="v"></span></li>
    <li><span class="n">5.</span><span class="t">I have a tooth or mouth problems that make it hard for me to eat<br><span style="margin-left:22px">2</span></span><span class="v"></span></li>
    <li><span class="n">6.</span><span class="t">I don't always have enough money to buy food</span><span class="v">4</span></li>
    <li><span class="n">7.</span><span class="t">I eat alone most of the time</span><span class="v">1</span></li>
    <li><span class="n">8.</span><span class="t">I have three or more different prescribed drugs or over-the counter drugs per day</span><span class="v">1</span></li>
    <li><span class="n">9.</span><span class="t">Without wanting to, I have gained or lost ten pounds in the last six months</span><span class="v">2</span></li>
    <li><span class="n">10.</span><span class="t">I am not always physically able to shop, cook or feed myself</span><span class="v">2</span></li>
  </ol>
  <div class="block" style="top:643px;left:416px">Total: <span class="u" style="width:26px"></span></div>

  <div class="risk-box">
    0-2: Low Nutritional Risks:<br>
    <i>Continue to evaluate Patient's nutritional needs and intervene as needed.</i><br>
    3-5: Moderate Nutritional Risk:<br>
    <i>Educate patient/family/caregiver and improve Patient's eating habits and lifestyle.</i><br>
    6+: High Nutritional Risk:<br>
    <i>Notify MD for further orders if indicated and consider special diet.</i>
  </div>

  <div class="bar bar--short" style="top:652px">Exercise</div>
  <div class="block" style="top:655px;left:153px;right:36px;line-height:12px">
    <div class="cols"><span>less than 1 hr week</span><span style="margin-left:60px">2-5 hr. per week</span><span>more than 6 hours per week</span></div>
  </div>

  <div class="bar" style="top:672px">Immunizations &amp; Screen test</div>
  <div class="block" style="top:689px;right:40px;line-height:10px">
    <div class="cols"><span>Immunizations: Flu Yes __ No __ Date _____</span><span>Pneumonia Yes __ No __ Date ________</span></div>
    Screening: Cholesterol level Yes __ No __ Date _____ Colon cancer screen Yes __ No __ Date ________<br>
    <div class="cols"><span>Mammogram Yes __ No __ Date _____</span><span style="margin-right:6px">Prostate cancer screen Yes __ No __ Date ________</span></div>
    Pertinent Lab Results: <span class="u" style="width:272px;height:7px"></span>
  </div>

  <div class="footer footer--blue" style="width:144px"></div>
  <div class="footer footer--green" style="left:218px;width:332px"></div>
</section>

</body>
</html>
```